Brightvale Cherries Rainier POS Card 7"H x 11"W

We are wanting to create a one-sided 7 x 11 Rainier cherry card that is eye catching and informative.This should be clear and easy to read and not cluttered. We use these cards as a display in grocery stores, demo stands, and other events to market Brightvale Rainier Cherries. We have a few facts that we would like displayed on the card (see below).

Target Market(s)

Consumers

Industry/Entity Type

Agriculture

Font styles to use
Sans Serif

Requirements
Must have
• Yellow cherries - yellow fruit (the blush on the skin is a kiss from the sun)
• Juice doesn't stain - Kid Friendly
• Add contrast to your summer table
• Sweetest Variety - still low glycemic
• Source of Vitamin C, Source of Potassium, and Source of Melatonin
• Rainiers take up to 4x as much work as red cherries
• Natural Color palettes
• Easy to read
• Brightvale Cherries
Nice to have
• Unique, creative, realistc Rainier cherry designs
Should not have
• pastel or neon color scheme, overly cutesy elements

```html
<!DOCTYPE html>
<html lang="en">
<head>
<meta charset="utf-8">
<title>Rainier Cherry Season – Brightvale Cherries</title>
<link rel="stylesheet" href="https://fonts.googleapis.com/css2?family=Archivo:wght@400;800&family=Oswald:wght@500&family=Alegreya:ital@1&display=swap">
<style>
  :root {
    --card-bg: #ffffff;
    --title-red: #e3202f;
    --band-gold: #f9d46c;
    --ink: #111111;
    --badge-wine: #7f2541;
    --badge-text: #ffffff;
    --photo-red: #d8403c;
    --photo-gold: #f4c56a;
    --photo-cream: #f6e6c4;
  }
  * { margin: 0; padding: 0; box-sizing: border-box; }
  html, body { width: 764px; height: 1200px; overflow: hidden; background: var(--card-bg); }
  .card { position: relative; width: 764px; height: 1200px; background: var(--card-bg); font-family: "Archivo", Arial, sans-serif; color: var(--ink); }

  .season-title { position: absolute; left: 20px; top: 24px; width: 84px; height: 1150px; }
  .season-title text { font-family: "Oswald", "Arial Narrow", sans-serif; font-weight: 500; fill: var(--title-red); }

  .hero-photo {
    position: absolute; left: 119px; top: 28px; width: 613px; height: 394px;
    background:
      radial-gradient(circle at 25% 25%, var(--photo-red) 0 14%, transparent 30%),
      radial-gradient(circle at 70% 45%, var(--photo-red) 0 12%, transparent 28%),
      radial-gradient(circle at 45% 75%, var(--photo-red) 0 14%, transparent 30%),
      radial-gradient(circle at 85% 80%, var(--photo-gold) 0 12%, transparent 28%),
      linear-gradient(135deg, var(--photo-gold), var(--photo-red) 55%, var(--photo-cream));
  }
  .gold-band { position: absolute; left: 119px; width: 613px; height: 33px; background: var(--band-gold); }
  .gold-band--top { top: 422px; }
  .gold-band--bottom { top: 1011px; }

  .facts { position: absolute; left: 134px; top: 488px; width: 560px; }
  .fact { margin-bottom: 24px; }
  .fact h2 { font-weight: 800; font-size: 28px; line-height: 34px; letter-spacing: 0.3px; }
  .fact p { font-weight: 400; font-size: 22.5px; line-height: 32px; }
  .fact--first p { margin-left: 4px; }
  .fact--work { margin-top: 22px; }

  .contrast-badge { position: absolute; left: 484px; top: 603px; width: 222px; height: 222px; }
  .contrast-badge text { font-family: "Alegreya", Georgia, serif; font-style: italic; font-size: 22px; fill: var(--badge-text); letter-spacing: 0.5px; }

  .brand { position: absolute; left: 0; right: 0; top: 1080px; display: flex; justify-content: center; align-items: center; gap: 14px; padding-left: 120px; }
  .brand-dot { width: 44px; height: 44px; border-radius: 50%; background: var(--ink); }
  .brand-name { font-family: "Archivo", Arial, sans-serif; font-weight: 800; font-size: 38px; color: var(--ink); }
</style>
</head>
<body>
<main class="card">
  <svg class="season-title" viewBox="0 0 84 1150" aria-label="Rainier Cherry Season">
    <text transform="translate(4 0) rotate(90)" x="0" y="0" font-size="108" textLength="1150" lengthAdjust="spacingAndGlyphs">RAINIER CHERRY SEASON</text>
  </svg>

  <div class="hero-photo" role="img" aria-label="Photo of a bowl of ripe yellow and red-blushed Rainier cherries with stems"></div>
  <div class="gold-band gold-band--top"></div>

  <section class="facts">
    <div class="fact fact--first">
      <h2>YELLOW FRUIT</h2>
      <p>(the blush on the skin is a kiss from the sun)</p>
    </div>
    <div class="fact">
      <h2>KID FRIENDLY</h2>
      <p>Juice that doesn’t stain</p>
    </div>
    <div class="fact">
      <h2>SWEETEST VARIETY</h2>
      <p>Low glycemic<br>Source of Vitamin C<br>Source of Potassium<br>and Source of Melatonin</p>
    </div>
    <div class="fact fact--work">
      <h2>RAINIERS WORK</h2>
      <p>Take up to 4x as much work as red cherries</p>
    </div>
  </section>

  <svg class="contrast-badge" viewBox="0 0 222 222" aria-label="Adds contrast to your summer table!">
    <circle cx="111" cy="111" r="108" fill="none" stroke="var(--badge-wine)" stroke-width="5" stroke-dasharray="0 12.3" stroke-linecap="round"/>
    <circle cx="111" cy="111" r="97" fill="var(--badge-wine)"/>
    <g transform="rotate(-8 111 111)" text-anchor="middle">
      <text x="111" y="86">Adds contrast</text>
      <text x="111" y="118">to your</text>
      <text x="111" y="150">summer table!</text>
    </g>
  </svg>

  <div class="gold-band gold-band--bottom"></div>

  <div class="brand">
    <span class="brand-dot"></span>
    <span class="brand-name">Brightvale Cherries</span>
  </div>
</main>
</body>
</html>
```